Web Design Project

We are an IT System Integrator. We provide Quillon 450 ERP System, CRM etc. We also provide hardware, networking servicing. Please look at www.trevantech.com.sg. They provide the same service as us. We like to redesign our web site. I will attached the color that I prefer for reference.
Updates

Our website is www.korbix.com.sg.  It has been created about 14 years ago.  We are trying to revamp it with a new look and information.   The new website must be informative, fast.    I have attached an attachment which show the color that I prefer(brownish golden).   

Our competitor (www.trevantech.com) is carrying the same trade as us.  They have all the informations In their website that we will like to have.  Therefore I recommend you to take a look at my competitor website and have a better   
understanding on the kind of information I would like to have for my new website.

This project is guarantee to the person with the best design.  We can have it guarantee.

Target Market(s)

Corporate and companies

Industry/Entity Type

Hardware

```html
<!DOCTYPE html>
<html lang="en">
<head>
<meta charset="utf-8">
<title>Korbix Information Systems</title>
<link href="https://fonts.googleapis.com/css2?family=Arimo:wght@400;700&family=Michroma&family=PT+Sans+Narrow:wght@700&family=Ubuntu:wght@400;500;700&display=swap" rel="stylesheet">
<style>
:root{
  --gold:#c0802f;
  --gold-light:#d79a48;
  --gold-dark:#9a6220;
  --ink:#222;
  --dark:#2e2e2e;
  --nav:#1c1c1c;
  --page:#eeeff1;
  --panel:#f3f3f3;
  --line:#c9c9c9;
  --muted:#777;
  --footer:#353535;
}
*{box-sizing:border-box;margin:0;padding:0}
html,body{width:1190px;height:1200px;overflow:hidden}
body{position:relative;background:linear-gradient(#e9eaec 0,#f6f6f7 380px,#dcdddf 384px,#f4f4f5 470px,#fff 700px);font-family:"Arimo",Arial,sans-serif;color:var(--ink)}
.abs{position:absolute}
.top-band{left:0;top:0;width:1190px;height:7px;background:var(--gold)}
.top-links{left:656px;top:0;width:296px;height:24px;background:var(--gold);border-radius:0 0 10px 10px;display:flex;justify-content:center;align-items:center;gap:7px;font-size:10px;color:#fff}
.top-links span.sep{opacity:.9}
.brand{left:256px;top:36px;display:flex;align-items:center;gap:10px}
.brand-mark{width:44px;height:44px;border-radius:50%;background:radial-gradient(circle at 35% 35%,var(--gold-light),var(--gold-dark))}
.brand-name{font-family:"Ubuntu",sans-serif;font-weight:500;font-size:11px;line-height:21px;color:var(--gold)}
.phones{right:244px;top:82px;text-align:right;font-family:"Ubuntu",sans-serif;color:#333}
.phones .row{display:flex;align-items:center;justify-content:flex-end;gap:4px;font-size:16px;height:28px}
.phones strong{color:var(--gold);font-size:20px;font-weight:700}
.main-nav{left:226px;top:136px;width:743px;height:38px;background:var(--nav);border-radius:6px 6px 0 0;display:flex;align-items:center;font-family:"Arimo",sans-serif;font-weight:700;font-size:12px;color:#fff}
.main-nav .item{height:38px;display:flex;align-items:center;padding:0 17px;border-right:1px solid #3a3a3a}
.main-nav .item.active{background:var(--gold);border-radius:6px 0 0 0;padding:0 9px}
.search{margin-left:auto;margin-right:6px;width:132px;height:27px;background:#fff;border-radius:3px;display:flex;align-items:center;justify-content:space-between;padding:0 6px;font-weight:400;font-size:9px;color:#555}
.nav-strip{left:226px;top:174px;width:743px;height:7px;background:var(--gold)}
.hero{left:226px;top:181px;width:743px;height:261px;background:#fff;overflow:hidden}
.hero svg.shape{position:absolute;left:0;top:0}
.hero-art{position:absolute;left:420px;top:0;width:300px;height:261px;background:radial-gradient(ellipse at 50% 40%,#6d6d6d 0,#8a8a8a 28%,rgba(198,132,52,.8) 42%,rgba(255,255,255,0) 70%)}
.hero-title{position:absolute;left:80px;top:32px;font-family:"Michroma",sans-serif;font-size:20px;line-height:27px;letter-spacing:2px;color:#fff}
.hero-text{position:absolute;left:77px;top:116px;width:245px;font-family:"PT Sans Narrow",sans-serif;font-weight:700;font-size:14px;line-height:21px;color:#fff}
.hero-btn{position:absolute;left:77px;top:209px;width:150px;height:29px;border-radius:15px;background:linear-gradient(var(--gold-light),var(--gold-dark));color:#fff;font-family:"Arimo",sans-serif;font-weight:700;font-size:13px;display:flex;align-items:center;justify-content:center}
.arrow{width:24px;height:32px;background:#fff;box-shadow:0 1px 3px rgba(0,0,0,.3);display:flex;align-items:center;justify-content:center;top:288px}
.welcome{left:252px;top:474px;display:flex;align-items:center;gap:10px}
.welcome-mark{width:22px;height:38px;border-radius:4px;background:linear-gradient(var(--gold-light),var(--gold-dark))}
.welcome h1{font-weight:400;font-size:16px;color:var(--gold)}
.welcome h1 b{font-size:19px;color:var(--ink)}
.welcome h1 em{font-style:normal;font-size:19px}
.rule{left:252px;top:516px;width:695px;border-top:1px dotted #999}
.intro{left:252px;top:532px;width:700px;font-size:8.7px;line-height:14.4px;color:#222}
.card{top:650px;width:218px;height:232px;background:var(--panel);border:1px solid var(--line);box-shadow:0 6px 8px -6px rgba(0,0,0,.35)}
.card-photo{position:absolute;left:9px;top:9px;width:199px;height:90px}
.card h2{position:absolute;left:14px;top:112px;font-weight:400;font-size:14px;color:#333}
.card h2 span{color:var(--gold)}
.card ul{position:absolute;left:14px;top:141px;list-style:none;font-size:9.5px;line-height:15px;color:#333}
.card li::before{content:"» ";font-weight:700}
.card .more{position:absolute;right:13px;bottom:10px;font-size:9.5px;color:#333}
.card .more span{color:var(--gold)}
.contact{left:726px;top:650px;width:218px;height:232px;background:var(--panel);border:1px solid var(--line)}
.contact h2{text-align:center;margin-top:10px;font-weight:700;font-size:16px;letter-spacing:-.5px;color:#333}
.contact h2 span{color:var(--gold)}
.field{margin:4px auto 0;width:188px;height:19px;background:#fff;border:1px solid #c4c4c4;border-radius:2px;font-size:8.5px;color:#777;padding:4px 8px;position:relative}
.field.select::after{content:"▾";position:absolute;right:2px;top:2px;width:11px;height:11px;border:1px solid #999;font-size:8px;line-height:10px;text-align:center;color:#444}
.field.comments{height:52px}
.actions{display:flex;gap:6px;margin:6px 0 0 14px}
.btn{height:20px;display:flex;align-items:center;border:1px solid #c4c4c4;background:#fff;font-size:11px;color:#333}
.btn .label{padding:0 8px}
.btn .tick{width:22px;height:18px;background:var(--gold);display:flex;align-items:center;justify-content:center}
.btn.clear .label{color:#999;padding:0 10px}
.partners{left:250px;top:922px;width:692px;height:77px;background:linear-gradient(#fff,#ececec);border:1px solid var(--line);border-radius:4px;display:flex;align-items:center;justify-content:space-around;padding:0 36px;font-family:"Arimo",sans-serif;font-weight:700;font-size:17px;color:#333}
.p-arrow{top:950px;width:22px;height:22px;background:#8c8c8c;border-radius:3px;display:flex;align-items:center;justify-content:center}
.footer{left:0;top:1034px;width:1190px;height:138px;background:var(--footer)}
.f-col{position:absolute;font-size:8.5px;color:#cfcfcf}
.f-col h3{font-size:10.5px;font-weight:700;color:var(--gold);margin-bottom:12px}
.f-col ul{list-style:none}
.f-col li{width:80px;border-bottom:1px dotted #777;line-height:14px;padding-left:12px;position:relative}
.f-col li::before{content:"»";position:absolute;left:0}
.f-col.wide li{width:96px}
.vline{position:absolute;top:32px;height:90px;border-left:1px dotted #777}
.social{font-family:"Ubuntu",sans-serif;font-size:12px;font-weight:500;color:#ddd;display:flex;align-items:center;gap:8px;height:30px}
.social .sq{width:17px;height:17px;background:#3b75b5;border-radius:2px}
.f-brand{position:absolute;left:778px;top:24px;display:flex;align-items:center;gap:10px}
.f-brand .mark{width:52px;height:40px;border-radius:50%;background:radial-gradient(circle at 40% 40%,#aaa,#555)}
.f-brand .name{font-family:"Ubuntu",sans-serif;font-size:8.5px;line-height:14px;color:var(--gold);font-weight:500}
.subscribe{position:absolute;left:780px;top:80px}
.subscribe h3{font-family:"Ubuntu",sans-serif;font-size:13px;font-weight:500;color:#ddd;margin-bottom:5px}
.subscribe .row{display:flex;gap:5px;align-items:center}
.subscribe .input{width:104px;height:15px;background:#fff;border-radius:2px;font-size:8px;color:#999;padding:2px 5px}
.subscribe .go{height:13px;padding:0 4px;background:var(--gold);border-radius:3px;font-size:7.5px;color:#fff;line-height:13px}
.copyright{left:0;top:1172px;width:1190px;height:28px;background:var(--gold);color:#fff;font-size:10px;display:flex;align-items:center;justify-content:center}
</style>
</head>
<body>
<div class="abs top-band"></div>
<nav class="abs top-links"><span>Home</span><span class="sep">|</span><span>Log Incident</span><span class="sep">|</span><span>Enquiry</span><span class="sep">|</span><span>Contact</span><span class="sep">|</span><span>Client Support</span></nav>

<header class="abs brand">
  <div class="brand-mark"></div>
  <div class="brand-name">KORBIX<br>INFORMATION<br>SYSTEMS PTE LTD</div>
</header>

<div class="abs phones">
  <div class="row">
    <svg width="16" height="16" viewBox="0 0 16 16"><path d="M3 1l3 3-1.5 2c1 2 3 4 5 5l2-1.5 3 3-2 2C7 14 2 9 1 3z" fill="#a86a28"/></svg>
    Phone #: <strong>(065) 6190-4417</strong></div>
  <div class="row">Toll Free Phone#: <strong>018.300.5512</strong></div>
</div>

<nav class="abs main-nav">
  <div class="item active">COMPANY</div>
  <div class="item">PRODUCTS</div>
  <div class="item">QUILLON</div>
  <div class="item">SERVICES</div>
  <div class="item">CLIENTELE</div>
  <div class="item">CAREERS</div>
  <div class="item" style="border:0">INFOBIN</div>
  <div class="search">Search here
    <svg width="20" height="18" viewBox="0 0 20 18"><circle cx="8" cy="7" r="5.5" fill="none" stroke="#c0802f" stroke-width="2"/><path d="M12 11l6 5" stroke="#c0802f" stroke-width="2.5"/></svg>
  </div>
</nav>
<div class="abs nav-strip"></div>

<section class="abs hero">
  <div class="hero-art" role="img" aria-label="Illustration of figures assembling a round puzzle"></div>
  <svg class="shape" width="743" height="261" viewBox="0 0 743 261">
    <path d="M0 0H300C440 40 470 180 370 261H0Z" fill="#c0802f"/>
    <path d="M0 0H286C425 42 452 182 356 261H0Z" fill="#8a8a8a"/>
    <path d="M0 0H265C400 44 420 182 338 261H0Z" fill="#2f2f2f"/>
  </svg>
  <div class="hero-title">KORBIX<br>INFORMATION<br>SYSTEMS PTE LTD</div>
  <p class="hero-text">For more than 20 years, Quillon has provided reliable software solutions optimized to take advantage of new technologies and meet the unique requirements of companies.</p>
  <div class="hero-btn">Click to Read More</div>
</section>
<div class="abs arrow" style="left:222px"><svg width="12" height="16"><path d="M10 2L3 8l7 6" fill="none" stroke="#111" stroke-width="3"/></svg></div>
<div class="abs arrow" style="left:950px"><svg width="12" height="16"><path d="M2 2l7 6-7 6" fill="none" stroke="#111" stroke-width="3"/></svg></div>

<div class="abs welcome">
  <div class="welcome-mark"></div>
  <h1>Welcome to <b>KORBIX INFORMATION</b> <em>SYSTEMS</em></h1>
</div>
<div class="abs rule"></div>
<p class="abs intro">Lorem ipsum dolor sit amet, consectetuer adipiscing elit, sed diam nonummy nibh euismod tincidunt ut laoreet dolore magna aliquam erat volutpat. Ut wisi enim ad minim veniam, quis nostrud exerci tation ullamcorper suscipit lobortis nisl ut aliquip ex ea commodo consequat. Duis autem vel eum iriure dolor in hendrerit in vulputate velit esse molestie consequat, vel illum dolore eu feugiat nulla facilisis at vero eros et accumsan et iusto odio dignissim qui blandit praesent luptatum zzril delenit augue duis dolore te feugait nulla Lorem ipsum dolor sit amet, consectetuer adipiscing elit, sed diam nonummy nibh euismod tincidunt ut laoreet dolore magna aliquam erat volutpat. Ut wisi enim ad minim veniam, quis nostrud exerci tation ullamcorper suscipit lobortis nisl ut aliquip ex ea commodo consequat. Duis autem vel eum iriure dolor in hendrerit in vulputate velit esse molestie consequat, vel illum dolore eu feugiat nulla facilisis at vero eros et accumsan et iusto odio dignissim qui blandit praesent luptatum zzril delenit augue duis dolore te feugait nullai.</p>

<article class="abs card" style="left:252px">
  <div class="card-photo" role="img" aria-label="Photo of a server room aisle" style="background:linear-gradient(90deg,#222,#777 50%,#222)"></div>
  <h2>Managed <span>IT Services</span></h2>
  <ul><li>Migrations &amp; Upgrades to the 9's</li><li>Report Development</li><li>Custom Applications Development</li><li>Technical and CNC</li></ul>
  <div class="more">Read <span>More</span></div>
</article>
<article class="abs card" style="left:488px">
  <div class="card-photo" role="img" aria-label="Photo of a globe beside server racks" style="background:linear-gradient(90deg,#1e6fc8,#5aa5ea 40%,#333 55%,#111)"></div>
  <h2>IT Consulting <span>Services</span></h2>
  <ul><li>Orvale Software and Technology Reseller</li><li>Ongoing Consultation</li><li>Consulting Services for World</li><li>Software Integration</li></ul>
  <div class="more">Read <span>More</span></div>
</article>
<aside class="abs contact">
  <h2>Quick <span>Contact</span></h2>
  <div class="field">Name:</div>
  <div class="field">Company:</div>
  <div class="field">E-mail:</div>
  <div class="field">Phone:</div>
  <div class="field select">Areas of Interest:</div>
  <div class="field comments">Comments:</div>
  <div class="actions">
    <div class="btn"><span class="label">Submit</span><span class="tick"><svg width="12" height="10"><path d="M1 5l4 4 6-8" fill="none" stroke="#fff" stroke-width="2"/></svg></span></div>
    <div class="btn clear"><span class="label">Clear</span><span class="tick"><svg width="12" height="10"><path d="M1 5l4 4 6-8" fill="none" stroke="#fff" stroke-width="2"/></svg></span></div>
  </div>
</aside>

<div class="abs partners"><span>Nimbusoft</span><span>Hexpoint</span><span>Ironbyte</span><span>Sentrilock</span><span>Delvo</span><span>Gridfy</span></div>
<div class="abs p-arrow" style="left:246px"><svg width="10" height="12"><path d="M8 1L3 6l5 5" fill="none" stroke="#fff" stroke-width="2"/></svg></div>
<div class="abs p-arrow" style="left:926px"><svg width="10" height="12"><path d="M2 1l5 5-5 5" fill="none" stroke="#fff" stroke-width="2"/></svg></div>

<footer class="abs footer">
  <div class="f-col" style="left:242px;top:28px"><h3>Quick Links</h3>
    <ul><li>Company</li><li>Products</li><li>Quillon</li><li>Services</li><li>Clientele</li></ul></div>
  <div class="f-col" style="left:355px;top:53px">
    <ul><li>Careers</li><li>Infobin</li><li>Enquiry</li><li>Sitemap</li><li>Contact</li></ul></div>
  <div class="vline" style="left:465px"></div>
  <div class="f-col wide" style="left:493px;top:28px"><h3>Support Center</h3>
    <ul><li>Free Assessment</li><li>Client Portal Login</li><li>Laecieas Deugtrat</li><li>Maecieas feiogtrat</li><li>Free Assessment</li></ul></div>
  <div class="vline" style="left:621px"></div>
  <div class="f-col" style="left:642px;top:28px"><h3>Connect with Us</h3>
    <div class="social" style="margin-top:6px">Linkora <span class="sq"></span></div>
    <div style="width:82px;border-top:1px dotted #777;margin:6px 0 8px"></div>
    <div class="social">Facenet <span class="sq"></span></div></div>
  <div class="vline" style="left:756px"></div>
  <div class="f-brand"><div class="mark"></div><div class="name">KORBIX<br>INFORMATION<br>SYSTEMS PTE LTD</div></div>
  <div class="subscribe"><h3>Subscribe with Us</h3>
    <div class="row"><div class="input">email address</div><div class="go">Subscribe</div></div></div>
</footer>
<div class="abs copyright">© Copyrights 2013. Korbix Information Systems. All Rights Reserved.</div>
</body>
</html>
```